Stationary Design to Complement our Website

We would like template designed for word documents that we can use for headed paper. The template should complement the style of our website & incorporate our existing logo. https://www.palvenroutes.com/

The header and footer design should be sperate PNG or JPEG files that we can copy and paste into word header and footers. They should work on A4 & letter sized papers.

Note the main web colours are as follows:

Black
HEX code #2b2c2b
C=71 M=64 Y=64 K=65
RGB 43,44,43

Green
HEX code #116c49
C=88 M=33 Y=82 K=24
RGB 17,108,73

Current fonts are ALEO & Gilroy.

Fonts and colours in new design don't have to match website exactly but should be complementary.
Updates

Made some updates to the brief

Font styles to use
Serif

Requirements
Must have
• a simple design that complements our website.
Some kind of graphic on the top & some sort of graphic on the bottom. Not just plain logo on top.
designs that incorporate the clouds might look good
Can also incorporate 5* rate marsh rating
Should not have
• no photographs included on the design

```html
<!DOCTYPE html>
<html lang="en">
<head>
<meta charset="utf-8">
<title>Palven Routes – Letterhead</title>
<link href="https://fonts.googleapis.com/css2?family=Aleo:wght@400;600&family=Outfit:wght@200;400;700&display=swap" rel="stylesheet">
<style>
  :root {
    --green: #1b7d2a;
    --green-soft: #a9c9ad;
    --ink: #111111;
    --paper: #ffffff;
  }
  * { margin: 0; padding: 0; box-sizing: border-box; }
  html, body { width: 848px; height: 1200px; overflow: hidden; background: var(--paper); }
  .letterhead { position: relative; width: 848px; height: 1200px; overflow: hidden; font-family: "Outfit", sans-serif; color: var(--ink); }
  .band { position: absolute; left: 0; width: 848px; }
  .band--top { top: 0; height: 160px; }
  .band--bottom { bottom: 0; height: 150px; }

  .brand { position: absolute; left: 56px; top: 26px; display: flex; align-items: flex-start; gap: 12px; }
  .brand__dot { width: 16px; height: 16px; border-radius: 50%; background: var(--paper); margin-top: 6px; }
  .brand__name { font-family: "Aleo", serif; font-weight: 400; color: var(--paper); font-size: 29px; line-height: 37px; letter-spacing: 3px; text-transform: uppercase; }

  .accent-disc { position: absolute; left: 676px; top: 94px; width: 96px; height: 96px; border-radius: 50%; background: var(--green); }

  .side-label { position: absolute; left: 54px; top: 940px; transform-origin: 0 0; transform: rotate(-90deg); font-family: "Outfit", sans-serif; font-weight: 200; font-size: 40px; letter-spacing: 22.5px; color: var(--green-soft); white-space: nowrap; line-height: 1; margin-left: -20px; }

  .recipient { position: absolute; left: 91px; top: 232px; font-family: "Aleo", serif; font-size: 18px; line-height: 24.5px; color: #222; font-style: normal; }
  .letter-date { position: absolute; left: 91px; top: 326px; font-family: "Aleo", serif; font-size: 18px; color: #222; }

  .greeting { position: absolute; left: 91px; top: 414px; font-family: "Outfit", sans-serif; font-weight: 700; font-size: 31px; letter-spacing: -0.3px; }

  .letter-body { position: absolute; left: 131px; top: 490px; width: 548px; font-size: 14.3px; line-height: 20.5px; }
  .letter-body p { margin-bottom: 20.5px; }
  .sign-off { font-weight: 700; }

  .footer-address { position: absolute; left: 43px; top: 1136px; font-family: "Aleo", serif; font-weight: 600; color: var(--paper); font-size: 16.5px; line-height: 21px; font-style: normal; }
  .contact-title { position: absolute; left: 510px; top: 1121px; font-family: "Aleo", serif; font-weight: 600; color: var(--paper); font-size: 18px; letter-spacing: 0.3px; }
  .contact-list { position: absolute; left: 645px; top: 1120px; display: grid; grid-template-columns: 85px auto; grid-auto-rows: 20px; align-items: center; color: var(--paper); }
  .contact-list dt { font-weight: 700; text-transform: uppercase; font-size: 7.5px; letter-spacing: 0.2px; }
  .contact-list dd { font-style: italic; font-weight: 200; font-size: 10px; }
</style>
</head>
<body>
<main class="letterhead">
  <svg class="band band--top" viewBox="0 0 848 160" preserveAspectRatio="none" aria-hidden="true">
    <path d="M0 0 H848 V58 C760 60 720 62 640 74 C480 100 300 126 0 124 Z" fill="var(--green)"/>
    <path d="M0 132 C300 136 480 108 640 84 C720 72 790 66 848 66" fill="none" stroke="var(--green)" stroke-width="5"/>
  </svg>

  <div class="brand">
    <span class="brand__dot"></span>
    <div class="brand__name">Palven<br>Routes</div>
  </div>
  <div class="accent-disc" aria-hidden="true"></div>

  <div class="side-label">PLACEHOLDER TEXT</div>

  <address class="recipient">John Doe<br>Circleroad 55<br>42353, Stockton</address>
  <p class="letter-date">2020/03/16</p>

  <h1 class="greeting">Greetings John!</h1>

  <section class="letter-body">
    <p>Lorem ipsum dolor sit amet, consectetur adipiscing elit. Pellentesque facilisis aliquet est eget maximus. Vestibulum sapien urna, tincidunt vitae accumsan non, dictum ut nisl. Lorem ipsum dolor sit amet, consectetur adipiscing elit. In iaculis ut dui a sodales. Sed imperdiet lacinia elit sit amet facilisis.</p>
    <p>Mauris posuere velit nec est vehicula, quis blandit ligula scelerisque. Aenean eu sodales nisl. Vestibulum gravida lorem convallis lacus sollicitu­din condimentum. Duis molestie est non tortor pharetra, ut ultricies mi ornare. Fusce sit amet semper erat, at maximus ex. In nec est eros. Fusce dui velit, pharetra at augue sagittis, elementum consequat augue.</p>
    <p>Pellentesque id lacus quis sapien aliquet mollis quis at mauris. Nunc semper molestie rhoncus. Nullam pulvinar sodales enim. Nunc fringilla elementum eros, quis euismod diam porta sed. Suspendisse interdum tincidunt vestibulum. Ut dolor velit, tincidunt a vulputate vel, vestibulum vehicula arcu. Nam purus eros, ultricies quis purus vitae, facilisis auctor quam. Orci varius natoque penatibus et magnis dis parturient montes, nascetur ridiculus mus.</p>
    <p class="sign-off">Best regards,<br>Michael, Palven Routes</p>
  </section>

  <svg class="band band--bottom" viewBox="0 0 848 150" preserveAspectRatio="none" aria-hidden="true">
    <path d="M0 12 C200 0 400 26 600 20 C720 16 800 8 848 6" fill="none" stroke="var(--green)" stroke-width="5"/>
    <path d="M0 30 C200 18 400 40 600 34 C720 30 800 22 848 20 V150 H0 Z" fill="var(--green)"/>
  </svg>

  <address class="footer-address">Alder House, Brookvale Road,<br>Westmere, Co.Carrow, Ireland.</address>
  <div class="contact-title">CONTACT US:</div>
  <dl class="contact-list">
    <dt>International</dt><dd>+353 61 48203</dd>
    <dt>USA &amp; Canada</dt><dd>1800 555 0142</dd>
    <dt>UK Freezone</dt><dd>0800 555 7316</dd>
  </dl>
</main>
</body>
</html>
```